Copperleaf Motorized Shade Business Card

Hello, we've had our logo made. Now we are looking for a clean and cool looking business card. One side can just be the logo with any design elements that might look good with it. The other side will be Name, Phone Number and Email. There will not be an address on the card.

```html
<!DOCTYPE html>
<html lang="en">
<head>
<meta charset="UTF-8">
<title>Copperleaf Motorized Shade – Business Card</title>
<link href="https://fonts.googleapis.com/css2?family=Roboto:wght@400;500;700&display=swap" rel="stylesheet">
<style>
  :root {
    --backdrop: #ececec;
    --card-white: #ffffff;
    --navy: #0c3a72;
    --navy-text: #0d3570;
    --sky: #1a9fe0;
    --sun: #f5bf1f;
    --ink-grey: #4f5358;
  }
  * { margin: 0; padding: 0; box-sizing: border-box; }
  html, body {
    width: 1200px;
    height: 800px;
    overflow: hidden;
    background: var(--backdrop);
    font-family: "Roboto", Arial, sans-serif;
  }
  .canvas {
    position: relative;
    width: 1200px;
    height: 800px;
  }
  .card {
    position: absolute;
    width: 571px;
    height: 329px;
    overflow: hidden;
  }

  /* Contact side */
  .card-contact {
    left: 475px;
    top: 32px;
    background: var(--card-white);
  }
  .identity {
    position: absolute;
    right: 305px;
    top: 140px;
    text-align: right;
  }
  .identity-name {
    font-size: 20px;
    font-weight: 700;
    color: var(--navy-text);
    letter-spacing: 0.2px;
    line-height: 1.2;
  }
  .identity-role {
    font-size: 16px;
    font-weight: 500;
    color: var(--sky);
    line-height: 1.35;
  }
  .divider {
    position: absolute;
    left: 285px;
    top: 134px;
    width: 2px;
    height: 64px;
    background: var(--sun);
  }
  .contact-list {
    position: absolute;
    left: 304px;
    top: 132px;
    list-style: none;
  }
  .contact-item {
    display: flex;
    align-items: center;
    gap: 7px;
    height: 21px;
    font-size: 15.5px;
    color: var(--ink-grey);
  }
  .contact-icon {
    width: 13px;
    height: 13px;
    flex: none;
  }
  .edge-band {
    position: absolute;
    left: 0;
    bottom: 0;
    width: 571px;
    height: 11px;
  }

  /* Brand side */
  .card-brand {
    left: 170px;
    top: 406px;
    background: var(--navy);
    display: flex;
    align-items: center;
    justify-content: center;
  }
  .brand-lockup {
    display: flex;
    align-items: center;
    gap: 16px;
    margin-top: 10px;
  }
  .brand-dot {
    width: 34px;
    height: 34px;
    border-radius: 50%;
    background: var(--sun);
    flex: none;
  }
  .brand-name {
    color: var(--card-white);
    font-weight: 500;
    font-size: 34px;
    line-height: 1.15;
    letter-spacing: 1px;
    text-transform: uppercase;
  }
</style>
</head>
<body>
<main class="canvas">

  <section class="card card-contact" aria-label="Contact side">
    <div class="identity">
      <p class="identity-name">MARCUS ELLERY</p>
      <p class="identity-role">Managing Director</p>
    </div>
    <div class="divider"></div>
    <ul class="contact-list">
      <li class="contact-item">
        <svg class="contact-icon" viewBox="0 0 16 16" aria-hidden="true">
          <path fill="#0d3570" d="M2 5c0-2 2.5-3 6-3s6 1 6 3v1.5h-3.2V5H5.2v1.5H2zM4.5 7h7l2 6.5H2.5z"/>
          <circle cx="8" cy="10" r="1.6" fill="#fff"/>
        </svg>
        <span>+56927304416</span>
      </li>
      <li class="contact-item">
        <svg class="contact-icon" viewBox="0 0 16 16" aria-hidden="true">
          <path fill="#0d3570" d="M1 6.5 8 2l7 4.5V14H1z"/>
          <path fill="#fff" d="M3 7.2 8 10l5-2.8V6.2L8 9 3 6.2z"/>
        </svg>
        <span>marcus@copperleafmail.com</span>
      </li>
      <li class="contact-item">
        <svg class="contact-icon" viewBox="0 0 16 16" aria-hidden="true">
          <circle cx="8" cy="8" r="6.5" fill="none" stroke="#0d3570" stroke-width="1.6"/>
          <ellipse cx="8" cy="8" rx="2.6" ry="6.5" fill="none" stroke="#0d3570" stroke-width="1.2"/>
          <path d="M1.8 8h12.4" stroke="#0d3570" stroke-width="1.2"/>
        </svg>
        <span>www.copperleafweb.com</span>
      </li>
    </ul>
    <svg class="edge-band" viewBox="0 0 571 11" preserveAspectRatio="none" aria-hidden="true">
      <polygon points="0,0 288,0 282,11 0,11" fill="var(--sky)"/>
      <polygon points="291,0 571,0 571,11 285,11" fill="var(--navy)"/>
    </svg>
  </section>

  <section class="card card-brand" aria-label="Brand side">
    <div class="brand-lockup">
      <span class="brand-dot" aria-hidden="true"></span>
      <p class="brand-name">Copperleaf<br>Motorized Shade</p>
    </div>
  </section>

</main>
</body>
</html>
```